Pause Your Day And Browse- PYDB poster

I am the Vice President of Advocacy for the Coastline Shelfkeepers Guild. I am looking to have a set of posters made for PYDB (Pause Your Day and Browse) October 23. PYDB is a time when all school children in BC are encouraged to Pause Your Day and Browse for 15-20 minutes at some point in their day.

I would like to get a set of 2 digital posters designed (if possible it would be nice to have the option to print to both 11 x 17 and 8.5 x 11 paper). We need a poster that is high school (Grade 8-12) appropriate and one that is elementary (Grade k-7) appropriate. Both posters need to be replicated in French. All posters need to have the KWNU logo on them as well as the Coastline Shelfkeepers Guild Logo.

Here is a link to last year's successful design http://kwnu-example.org/csg/info/advocacy.html
There are two additional samples in the uploaded files section.

Each poster needs to have the following information:

-Pause Your Day and Browse (PYDB)
- The date Monday, October 23, 2017
-the logo for the KWNU (attached)
-the logo for the CSG (attached)- the logos do not have to be large.

Target Market(s)

Children ages 5-12 and 12-17 as well as their teachers

Industry/Entity Type

Teacher

Font styles to use
Sans Serif

Requirements
Must have
• Must have both logos- colours may be changed for either or both
Nice to have
• Clear, Bright lettering. Images of child or children enjoying reading
Should not have
• stereotypes

```html
<!DOCTYPE html>
<html lang="en">
<head>
<meta charset="utf-8">
<title>Pause Your Day And Browse – PYDB poster</title>
<link rel="stylesheet" href="https://fonts.googleapis.com/css2?family=Alfa+Slab+One&family=Dosis:wght@500;600&display=swap">
<style>
  :root {
    --backdrop: #f6eeee;
    --paper: #ffffff;
    --ink: #3a3a3a;
    --purple: #7b3f98;
    --yellow: #fff200;
    --pink: #e8828f;
    --green: #a9cf6b;
    --teal: #86c8c9;
    --orange: #f2c45a;
    --navy: #26407a;
    --line: #4a3a32;
  }
  * { box-sizing: border-box; margin: 0; padding: 0; }
  html, body { width: 1200px; height: 1200px; overflow: hidden; }
  body { background: var(--backdrop); position: relative; font-family: "Dosis", sans-serif; }

  .poster {
    position: absolute; left: 171px; top: 40px;
    width: 858px; height: 1120px;
    background: var(--paper); overflow: hidden;
  }
  .dots { position: absolute; inset: 0; width: 858px; height: 1120px; }

  .art { position: absolute; }
  .art--books-top-left   { left: 0;   top: 0;    width: 230px; height: 160px; border-radius: 0 0 90px 0; background: radial-gradient(circle at 45% 40%, var(--teal) 55%, rgba(134,200,201,0.25) 100%); }
  .art--book-top-right   { left: 620px; top: 0;  width: 238px; height: 220px; border-radius: 0 0 0 110px; background: radial-gradient(circle at 55% 40%, var(--green) 55%, rgba(169,207,107,0.25) 100%); }
  .art--book-left        { left: 0;   top: 335px; width: 185px; height: 345px; border-radius: 0 90px 90px 0; background: radial-gradient(circle at 40% 60%, var(--pink) 50%, rgba(232,130,143,0.25) 100%); }
  .art--book-right       { left: 758px; top: 315px; width: 100px; height: 275px; border-radius: 90px 0 0 90px; background: radial-gradient(circle at 70% 40%, var(--orange) 55%, rgba(242,196,90,0.25) 100%); }
  .art--book-lower-right { left: 695px; top: 680px; width: 163px; height: 235px; border-radius: 90px 0 0 90px; background: radial-gradient(circle at 65% 45%, var(--teal) 55%, rgba(134,200,201,0.25) 100%); }
  .art--books-bottom     { left: 460px; top: 1015px; width: 290px; height: 105px; border-radius: 110px 110px 0 0; background: radial-gradient(circle at 40% 80%, var(--pink) 50%, rgba(232,130,143,0.25) 100%); }
  .art--reader           { left: 20px; top: 735px; width: 345px; height: 345px; border-radius: 40% 40% 30% 30%; background: linear-gradient(180deg, #f3d6a9 0%, #f6dc7a 55%, #f1c9c9 100%); }

  .partners { position: absolute; top: 75px; left: 0; width: 858px; display: flex; justify-content: center; align-items: center; gap: 34px; }
  .partner { display: flex; align-items: center; gap: 8px; font-family: "Dosis", sans-serif; font-weight: 600; font-size: 26px; }
  .partner__mark { width: 22px; height: 22px; }
  .partner--union { color: var(--navy); }
  .partner--union .partner__mark { border-radius: 50%; background: var(--navy); }
  .partner--guild { color: var(--ink); flex-direction: column; gap: 2px; }
  .partner--guild .partner__name { font-size: 34px; line-height: 1; }
  .partner--guild .partner__full { font-size: 9px; letter-spacing: 0.5px; text-align: center; width: 110px; line-height: 1.2; }

  .title { position: absolute; left: 203px; top: 305px; width: 470px; height: 160px; font-family: "Alfa Slab One", serif; }
  .title__letter { position: absolute; font-size: 128px; line-height: 1; text-align: center; }
  .title__letter--p { left: 2px; top: 0; width: 130px; height: 145px; background: var(--yellow); color: #fff; padding-top: 6px; }
  .title__letter--y { left: 134px; top: 8px; width: 125px; color: var(--pink); border-top: 4px solid var(--pink); border-bottom: 4px solid var(--pink); height: 145px; padding-top: 4px; }
  .title__letter--d { left: 262px; top: 20px; width: 105px; color: var(--green); border-bottom: 3px solid var(--green); height: 140px; }
  .title__letter--b { left: 380px; top: 17px; width: 74px; height: 128px; background: var(--teal); color: #fff; font-size: 96px; padding-top: 14px; }

  .subtitle { position: absolute; top: 476px; left: 0; width: 858px; text-align: center; color: var(--ink); font-weight: 500; font-size: 43px; line-height: 44px; letter-spacing: 0.5px; }
  .event-date { position: absolute; top: 632px; left: 0; width: 858px; text-align: center; color: var(--purple); font-weight: 500; font-size: 44px; line-height: 44px; letter-spacing: 0.5px; }
  .event-date__o { display: inline-block; position: relative; }
  .event-date__o::before { content: ""; position: absolute; left: 5px; top: 13px; width: 26px; height: 26px; border-radius: 50%; background: #d9879b; z-index: -1; }
</style>
</head>
<body>
  <main class="poster">
    <div class="art art--books-top-left" role="img" aria-label="Line drawing of stacked books over a teal circle"></div>
    <div class="art art--book-top-right" role="img" aria-label="Line drawing of a closed book over a green circle"></div>
    <div class="art art--book-left" role="img" aria-label="Line drawing of an open book over pink circles"></div>
    <div class="art art--book-right" role="img" aria-label="Line drawing of a book over a yellow circle"></div>
    <div class="art art--book-lower-right" role="img" aria-label="Line drawing of a book over a teal circle"></div>
    <div class="art art--books-bottom" role="img" aria-label="Line drawing of a stack of books over a pink circle"></div>

    <svg class="dots" viewBox="0 0 858 1120" aria-hidden="true">
      <circle cx="304" cy="8" r="8" fill="var(--pink)"/>
      <circle cx="258" cy="194" r="5" fill="var(--green)"/>
      <circle cx="129" cy="258" r="8" fill="var(--teal)"/>
      <circle cx="639" cy="288" r="7" fill="var(--green)"/>
      <circle cx="735" cy="248" r="10" fill="var(--orange)"/>
      <circle cx="662" cy="409" r="10" fill="var(--pink)"/>
      <circle cx="738" cy="556" r="10" fill="var(--teal)"/>
      <circle cx="635" cy="631" r="8" fill="var(--green)"/>
      <circle cx="502" cy="845" r="40" fill="var(--yellow)"/>
      <circle cx="345" cy="949" r="10" fill="var(--teal)"/>
      <circle cx="633" cy="954" r="5" fill="var(--pink)"/>
      <circle cx="443" cy="1015" r="7" fill="var(--orange)"/>
      <circle cx="771" cy="1016" r="12" fill="var(--green)"/>
      <circle cx="703" cy="863" r="20" fill="var(--teal)"/>
    </svg>

    <header class="partners">
      <div class="partner partner--union"><span class="partner__mark"></span><span class="partner__name">KWNU</span></div>
      <div class="partner partner--guild"><span class="partner__name">CSG</span><span class="partner__full">COASTLINE SHELFKEEPERS GUILD</span></div>
    </header>

    <h1 class="title" aria-label="PYDB">
      <span class="title__letter title__letter--p">P</span>
      <span class="title__letter title__letter--y">Y</span>
      <span class="title__letter title__letter--d">D</span>
      <span class="title__letter title__letter--b">B</span>
    </h1>

    <p class="subtitle">PAUSE YOUR DAY<br>AND BROWSE</p>

    <p class="event-date">MONDAY<br><span class="event-date__o">O</span>CTOBER 23, 2017</p>

    <div class="art art--reader" role="img" aria-label="Cartoon of a cheerful child in a yellow shirt sitting with an open book, arms raised"></div>
  </main>
</body>
</html>
```